The Brindlewick Project

All information regarding the design is located at Brindlewick.com. Any questions regarding the project, will be answered on the site.

```html
<!DOCTYPE html>
<html lang="en">
<head>
<meta charset="utf-8">
<title>Brindlewick</title>
<link rel="stylesheet" href="https://fonts.googleapis.com/css2?family=Ubuntu:wght@400;500&display=swap">
<style>
  :root {
    --bar-top: #88308f;
    --bar-bottom: #5d1f69;
    --panel-top: #7b2a88;
    --panel-bottom: #4d1d5a;
    --brand: #4a2170;
    --ink-purple: #5a2266;
    --button-top: #f8f2fb;
    --button-bottom: #d7b6ea;
    --haze: #e5e2e8;
    --footer-bg: #f8f8f8;
    --footer-line: #ececec;
    --footer-text: #a6a6a6;
    --white: #ffffff;
  }
  * { margin: 0; padding: 0; box-sizing: border-box; }
  html, body { width: 1200px; height: 706px; overflow: hidden; }
  body {
    position: relative;
    background: var(--white);
    font-family: "Ubuntu", "Trebuchet MS", sans-serif;
  }
  .top-bar {
    position: absolute; left: 0; top: 0; width: 1200px; height: 44px;
    background: linear-gradient(var(--bar-top), var(--bar-bottom));
  }
  .main-nav { display: flex; position: absolute; left: 14px; top: 14px; list-style: none; }
  .main-nav li { color: var(--white); font-size: 13px; margin-right: 33px; letter-spacing: 0.1px; }
  .login-button {
    position: absolute; left: 1109px; top: 8px; width: 76px; height: 26px;
    background: linear-gradient(#ffffff, #e7e4ea);
    color: var(--ink-purple); font-size: 12px; line-height: 27px; text-align: center;
  }
  .header-haze {
    position: absolute; left: 0; top: 44px; width: 1200px; height: 90px;
    background: linear-gradient(var(--haze), var(--white));
  }
  .brand {
    position: absolute; left: 0; top: 222px; width: 1200px; text-align: center;
    font-size: 56px; font-weight: 400; color: var(--brand); letter-spacing: -0.5px;
  }
  .search-shadow {
    position: absolute; left: 210px; top: 380px; width: 780px; height: 22px;
    background: radial-gradient(ellipse at center, rgba(0,0,0,0.22), rgba(0,0,0,0) 70%);
  }
  .search-panel {
    position: absolute; left: 282px; top: 313px; width: 641px; height: 78px;
    border-radius: 4px;
    background: linear-gradient(var(--panel-top), var(--panel-bottom));
  }
  .search-field {
    position: absolute; left: 25px; top: 22px; width: 523px; height: 34px;
    background: linear-gradient(#ffffff 60%, #ebe8ee);
    color: var(--ink-purple); font-size: 13px; line-height: 35px; padding-left: 14px;
  }
  .search-button {
    position: absolute; left: 557px; top: 22px; width: 58px; height: 34px;
    background: linear-gradient(var(--button-top), var(--button-bottom));
    color: var(--ink-purple); font-size: 16px; font-weight: 500; line-height: 35px; text-align: center;
  }
  .site-footer {
    position: absolute; left: 0; top: 660px; width: 1200px; height: 46px;
    background: var(--footer-bg); border-top: 1px solid var(--footer-line);
    font-size: 11px; color: var(--footer-text);
  }
  .copyright { position: absolute; left: 15px; top: 18px; }
  .footer-links { position: absolute; left: 920px; top: 18px; display: flex; }
  .footer-links .divider { margin: 0 18px; }
</style>
</head>
<body>
  <header class="top-bar">
    <ul class="main-nav">
      <li>WEB</li><li>IMAGES</li><li>VIDEOS</li><li>NEWS</li><li>MAPS</li>
    </ul>
    <div class="login-button">LOGIN</div>
  </header>
  <div class="header-haze"></div>

  <main>
    <h1 class="brand">Brindlewick</h1>
    <div class="search-shadow"></div>
    <div class="search-panel">
      <div class="search-field">Ask your question here</div>
      <div class="search-button">GO</div>
    </div>
  </main>

  <footer class="site-footer">
    <span class="copyright">Copyright © 2013 Brindlewick. All rights reserved</span>
    <span class="footer-links"><span>Privacy Policy</span><span class="divider">|</span><span>Terms of use</span></span>
  </footer>
</body>
</html>
```